Life Coach for Lawyers Business Card Design

Elegant, original, business card design for life coaching service for associate attorneys who work in big law and struggle with stress, overwhelm, and time management. Double sided design.

Target Market(s)

Women associate attorneys who work in big law and struggle with stress, overwhelm, and time management.

Industry/Entity Type

Life Coaching

Contact Information for Business Card

Marlene Quorthby
Life Coach
519.607.4431
brightcounselpath.net
marlene@brightcounselpath.net
@brightcounselpath (Instagram)

Font styles to use
Other font styles liked:
• Silver South font duo. See uploaded files.

Requirements
Must have
• Icons for phone, website, email, and Instagram instead of words. Specific colors used in my logo (171B2B, 421121, FFFFFF)
Nice to have
• Foil. Embossed. Feminine design.
Should not have
• Any colors other than those used in logo. See uploaded files.

```html
<!DOCTYPE html>
<html lang="en">
<head>
<meta charset="utf-8">
<title>Bright Counsel Path — Business Card</title>
<link rel="stylesheet" href="https://fonts.googleapis.com/css2?family=Playfair+Display:wght@500&family=Oswald:wght@300;400&display=swap">
<style>
  :root {
    --navy: #171B2B;
    --wine: #421121;
    --wine-deep: #33101C;
    --white: #FFFFFF;
    --paper: #F4F4F2;
    --backdrop: #E6E6E6;
  }
  * { box-sizing: border-box; margin: 0; padding: 0; }
  html, body { width: 1200px; height: 1200px; overflow: hidden; }
  body {
    background: var(--backdrop);
    display: flex;
    flex-direction: column;
    align-items: center;
    justify-content: center;
    gap: 60px;
  }
  .card {
    width: 840px;
    height: 480px;
    position: relative;
    overflow: hidden;
    box-shadow: 0 10px 28px rgba(0,0,0,0.18);
  }
  /* Front */
  .card--front {
    background: linear-gradient(160deg, var(--wine) 0%, var(--wine-deep) 100%);
    display: flex;
    align-items: center;
    justify-content: center;
    padding: 0 80px;
  }
  .brand-name {
    font-family: "Playfair Display", serif;
    font-weight: 500;
    text-transform: uppercase;
    letter-spacing: 0.08em;
    line-height: 1.1;
    text-align: center;
  }
  .brand-name span { display: block; }
  .card--front .brand-name {
    color: var(--white);
    font-size: 64px;
  }
  /* Back */
  .card--back {
    background: var(--paper);
    display: flex;
    flex-direction: column;
  }
  .back-top {
    height: 268px;
    display: flex;
    flex-direction: column;
    align-items: center;
    justify-content: center;
    gap: 26px;
    padding-top: 10px;
  }
  .card--back .brand-name {
    color: var(--wine);
    font-size: 46px;
  }
  .identity { text-align: center; }
  .person-name {
    font-family: "Oswald", sans-serif;
    font-weight: 400;
    font-size: 28px;
    letter-spacing: 0.18em;
    color: var(--navy);
    text-transform: uppercase;
  }
  .person-title {
    font-family: "Oswald", sans-serif;
    font-weight: 300;
    font-size: 17px;
    letter-spacing: 0.32em;
    color: var(--navy);
    text-transform: uppercase;
    margin-top: 4px;
  }
  .person-title::before, .person-title::after {
    content: "•"; margin: 0 8px; letter-spacing: 0;
  }
  .contact-band {
    flex: 1;
    background: var(--navy);
    display: grid;
    grid-template-columns: 1fr 1.45fr;
    align-content: center;
    row-gap: 30px;
    column-gap: 30px;
    padding: 0 50px 0 90px;
  }
  .contact-item {
    display: flex;
    align-items: center;
    gap: 12px;
    font-family: "Oswald", sans-serif;
    font-weight: 300;
    font-size: 21px;
    letter-spacing: 0.08em;
    color: var(--white);
    text-transform: uppercase;
    white-space: nowrap;
  }
  .contact-item svg { width: 22px; height: 22px; flex: none; }
</style>
</head>
<body>

<section class="card card--front" aria-label="Card front">
  <h1 class="brand-name"><span>Bright Counsel</span><span>Path</span></h1>
</section>

<section class="card card--back" aria-label="Card back">
  <div class="back-top">
    <h2 class="brand-name">Bright Counsel Path</h2>
    <div class="identity">
      <p class="person-name">Marlene Quorthby</p>
      <p class="person-title">Life Coach</p>
    </div>
  </div>
  <div class="contact-band">
    <p class="contact-item contact-item--phone">
      <svg viewBox="0 0 24 24" fill="#FFFFFF"><path d="M6.6 10.8a15.1 15.1 0 006.6 6.6l2.2-2.2a1 1 0 011-.25 11.4 11.4 0 003.6.57 1 1 0 011 1V20a1 1 0 01-1 1A17 17 0 013 4a1 1 0 011-1h3.5a1 1 0 011 1c0 1.25.2 2.45.57 3.6a1 1 0 01-.25 1z"/></svg>
      519.607.4431
    </p>
    <p class="contact-item contact-item--email">
      <svg viewBox="0 0 24 24" fill="none" stroke="#FFFFFF" stroke-width="1.8"><rect x="2.5" y="5" width="19" height="14" rx="1"/><path d="M3 6l9 7 9-7"/></svg>
      marlene@brightcounselpath.net
    </p>
    <p class="contact-item contact-item--social">
      <svg viewBox="0 0 24 24" fill="none" stroke="#FFFFFF" stroke-width="1.8"><circle cx="12" cy="12" r="9"/></svg>
      @brightcounselpath
    </p>
    <p class="contact-item contact-item--web">
      <svg viewBox="0 0 24 24" fill="none" stroke="#FFFFFF" stroke-width="1.8"><circle cx="12" cy="12" r="9"/><path d="M3 12h18M12 3c2.8 3 2.8 15 0 18M12 3c-2.8 3-2.8 15 0 18"/></svg>
      brightcounselpath.net
    </p>
  </div>
</section>

</body>
</html>
```